Clean and Polished Store Design

Please design a website similar to this one: http://veltrasign.com/
We require two pages:
* the home page: http://veltrasign.com/
* the product page: http://veltrasign.com/products/our-printer
Notice that there are few words and more pictures. It's clean and professional. Although I think their product page is difficult to read because it is too spread out.
Please help us generate excitement for our product via a polished and high-end looking web design. Please keep it VERY SIMPLE.
Target Market(s)
Our target market is consumers that have never bought a 3D printer before and those to whom 3D printing is new but exciting. Our market is not very technical. They love the sleek look of the printer and its ease of use.
Industry/Entity Type
Printer
Requirements
Must have
- We require two pages:
- * the home page: http://veltrasign.com/
- * the product page: http://veltrasign.com/products/our-printer
- One of our product renderings must be displayed on both the homepage and the product page.
- Our logo must be displayed on both pages.
- The pages must have a header, a footer and content equivalent to the veltrasign website.

```html
<!DOCTYPE html>
<html lang="en">
<head>
<meta charset="utf-8">
<title>Cubriq 3D – Home</title>
<link rel="stylesheet" href="https://fonts.googleapis.com/css2?family=Arimo:wght@400;700&display=swap">
<style>
:root{
  --backdrop:#e6e6e6;
  --page:#ffffff;
  --ink:#2b2b2b;
  --accent:#1a93d0;
  --accent-strong:#0f9ad6;
  --rule:#dcdcdc;
  --footer:#333333;
  --footer-text:#ffffff;
  --field:#e9e9e9;
  --studio-light:#f2f2f2;
  --studio-mid:#d6d6d6;
  --studio-dark:#a8a8a8;
  --printer-orange:#ff9416;
  --printer-red:#b01818;
  --printer-white:#ffffff;
  --printer-blue:#1f6ff0;
}
*{margin:0;padding:0;box-sizing:border-box}
html,body{width:1064px;height:1200px;overflow:hidden}
body{background:var(--backdrop);font-family:"Arimo",Arial,sans-serif;color:var(--ink);position:relative}
.page{position:absolute;left:42px;top:0;width:980px;height:1200px;background:var(--page);box-shadow:0 0 8px rgba(0,0,0,.25)}
.abs{position:absolute}

.brand{left:63px;top:40px;font-size:42px;font-weight:700;color:#111;letter-spacing:-.5px;line-height:56px}
.header-divider{left:370px;top:36px;width:1px;height:68px;background:var(--rule)}
.main-nav a{position:absolute;top:59px;height:30px;line-height:30px;font-size:19px;color:var(--ink);text-decoration:none}
.main-nav .current{left:422px;width:94px;background:var(--accent-strong);color:#fff;border-radius:4px;padding-left:16px}

.hero-frame{left:46px;top:170px;width:639px;height:370px;border:1px solid var(--rule)}
.hero-image{left:62px;top:185px;width:605px;height:341px;
  background:
    radial-gradient(ellipse 32% 48% at 50% 50%,var(--printer-orange) 0%,rgba(255,148,22,.85) 45%,rgba(255,148,22,0) 100%),
    radial-gradient(ellipse 70% 25% at 50% 88%,rgba(230,120,10,.35) 0%,rgba(230,120,10,0) 100%),
    linear-gradient(180deg,var(--studio-mid) 0%,var(--studio-light) 45%,var(--studio-dark) 100%)}

.side-menu{left:730px;top:163px;width:188px}
.side-menu a{display:block;height:54.3px;line-height:54px;padding-left:17px;font-size:19px;color:var(--accent);text-decoration:none;border-bottom:1px dotted var(--rule)}
.side-menu a:last-child{border-bottom:none}

.rule{left:62px;width:856px;height:1px;border-top:1px dotted var(--rule)}
.colour-title{left:62px;top:592px;font-size:17px;color:var(--accent)}
.swatch{top:628px;width:191px;height:107px}
.swatch-orange{background:radial-gradient(ellipse 32% 50% at 50% 50%,var(--printer-orange) 0%,rgba(255,148,22,.8) 45%,rgba(255,148,22,0) 100%),linear-gradient(180deg,var(--studio-mid),var(--studio-light) 45%,var(--studio-dark))}
.swatch-red{background:radial-gradient(ellipse 32% 50% at 50% 50%,var(--printer-red) 0%,rgba(176,24,24,.8) 45%,rgba(176,24,24,0) 100%),linear-gradient(180deg,var(--studio-mid),var(--studio-light) 45%,var(--studio-dark))}
.swatch-white{background:radial-gradient(ellipse 32% 50% at 50% 50%,var(--printer-white) 0%,rgba(255,255,255,.85) 45%,rgba(255,255,255,0) 100%),linear-gradient(180deg,#9c9c9c,#c4c4c4 45%,#7e7e7e)}
.swatch-blue{background:radial-gradient(ellipse 32% 50% at 50% 50%,var(--printer-blue) 0%,rgba(31,111,240,.8) 45%,rgba(31,111,240,0) 100%),linear-gradient(180deg,var(--studio-mid),var(--studio-light) 45%,var(--studio-dark))}

.updates-title{left:59px;top:775px;font-size:25px;font-weight:700;letter-spacing:.3px}
.updates-text{left:59px;top:814px;width:680px;font-size:17px;line-height:21px}
.email{left:61px;top:873px;width:503px;height:33px;background:var(--field);border:1px solid #999;font:17px "Arimo",Arial,sans-serif;padding-left:11px;color:#333}
.subscribe{left:581px;top:873px;width:192px;height:33px;background:var(--accent-strong);color:#fff;border:none;font:700 17px "Arimo",Arial,sans-serif;letter-spacing:.3px}

.footer{left:0;top:975px;width:980px;height:225px;background:var(--footer);color:var(--footer-text)}
.footer-title{left:61px;top:22px;font-size:23px;font-weight:400}
.footer-text{left:65px;top:69px;width:836px;font-size:11.3px;line-height:14.6px}
.footer-text span{display:block;white-space:nowrap;text-align:justify;text-align-last:justify}
.social{top:149px;width:36px;height:37px;border-radius:2px}
.social-one{left:61px;background:#3b5998}
.social-two{left:134px;background:#4a8fc7}
.social-three{left:207px;background:#d24a36}
.footer-nav a{position:absolute;top:165px;font-size:14px;color:var(--accent);text-decoration:none}
</style>
</head>
<body>
<div class="page">
  <header>
    <div class="abs brand">Cubriq 3D</div>
    <div class="abs header-divider"></div>
    <nav class="main-nav">
      <a class="current" href="#">HOME</a>
      <a href="#" style="left:569px">ABOUT</a>
      <a href="#" style="left:684px">PRODUCTS</a>
      <a href="#" style="left:827px">CONTACT</a>
    </nav>
  </header>

  <main>
    <div class="abs hero-frame"></div>
    <div class="abs hero-image" role="img" aria-label="Product rendering of the glossy orange cube-shaped 3D printer on a grey studio background"></div>

    <nav class="abs side-menu">
      <a href="#">OVERVIEW</a>
      <a href="#">TECH SPECS</a>
      <a href="#">PRICE</a>
      <a href="#">SUPPORT</a>
      <a href="#">PRE-ORDER</a>
      <a href="#">LOREM IPSUM</a>
      <a href="#">LOREM IPSUM</a>
    </nav>

    <div class="abs rule" style="top:582px"></div>
    <div class="abs colour-title">Choose your favorite color.</div>
    <div class="abs swatch swatch-orange" style="left:62px" role="img" aria-label="Orange printer variant rendering"></div>
    <div class="abs swatch swatch-red" style="left:283px" role="img" aria-label="Red printer variant rendering"></div>
    <div class="abs swatch swatch-white" style="left:506px" role="img" aria-label="White printer variant rendering"></div>
    <div class="abs swatch swatch-blue" style="left:727px" role="img" aria-label="Blue printer variant rendering"></div>
    <div class="abs rule" style="top:759px"></div>

    <section>
      <h2 class="abs updates-title">LAST UPDATES</h2>
      <p class="abs updates-text">This is Draftwell's version &nbsp;of Lorem Ipsum. Proin gravida nibh vel velit auctor ali-<br>quet. Aenean sollicitudin, lorem quis bibendum auctor, nisi elit consequat ipsum, nec</p>
      <input class="abs email" type="text" value="email adress...">
      <button class="abs subscribe">SUBSCRIBE</button>
    </section>
  </main>

  <footer class="abs footer">
    <h3 class="abs footer-title">Pre-Order now from Cubriq 3D</h3>
    <p class="abs footer-text">
      <span>This is Draftwell's version &nbsp;of Lorem Ipsum. Proin gravida nibh vel velit auctor aliquet. Aenean sollicitudin, lorem quis bibendum auctor, nisi elit conse-</span>
      <span>quat ipsum, nec sagittis sem nibh id elit. Duis sed odio sit amet nibh vulputate cursus a sit amet mauris. Morbi accumsan ipsum velit. Nam nec tellus a</span>
      <span>odio tincidunt auctor a ornare odio. Sed non &nbsp;mauris vitae erat consequat auctor eu in elit. Class aptent taciti sociosqu ad litora torquent per conubia</span>
      <span>nostra, per inceptos himenaeos. Mauris in erat justo. Nullam ac urna eu felis dapibus condimentum sit amet a augue. Sed non neque elit. Sed ut imperdi-</span>
    </p>
    <a class="abs social social-one" href="#" aria-label="Social profile"></a>
    <a class="abs social social-two" href="#" aria-label="Social profile"></a>
    <a class="abs social social-three" href="#" aria-label="Social profile"></a>
    <nav class="footer-nav">
      <a href="#" style="left:449px">HOME</a>
      <a href="#" style="left:581px">ABOUT</a>
      <a href="#" style="left:695px">PRODUCTS</a>
      <a href="#" style="left:838px">CONTACT</a>
    </nav>
  </footer>
</div>
</body>
</html>
```